Premium Lawn fertiliser packaging - Looking for long term designer

*Update at bottom
I need a carefully considered, bold and professional packaging design for my new premium lawn fertiliser product. This contest is for a detailed front of the stand-up pouch packaging and once I’ve chosen a winner, they’ll be asked to create the layout for the back that links to the front as well. I have a full range of additional products that will also need designs and so I'm looking for someone who can do a great job here and who we can work with long term.

The front should include our logo for Pemberly Turf Supply Direct and be titled “Bloom Vigor Max” "Professional Lawn Fertiliser". The spring fertiliser tag line is "Awaken your lawn: Lush Greening, Lasting Health".
Beneath it, it then needs to include some important usage information and the key benefits along with some suitable graphic.

Key information to include:

Apply March - June
Treats 35-50 m2
16-3-8
+2%MgO + 1% Fe + 2.9% CaO (this is the chemical makeup of the fertiliser and needs to be fairly prominent. If you look at other professional fertiliser packaging, you'll see how it needs to compare).

Key features:
Premium fertiliser, used by professionals
Advanced greening with micro-nutrient complex
Dual action Nitrogen: Instant green boost & continuous feed for 3 months
Child & pet safe

Our brand colours are purple and green. Purple = #592999, Green = 3cb64a / 81d742 / 4d9d44

I think these colours look great against a white background.

Please make sure you look at our website as well to get an idea of our brand: www.pemberlyturfsupply.co.uk

To help, I've attached images of competitors fertiliser packaging that I like the look of. I'm not looking for you to copy but just see what type of thing appeals to me, the standard I'm expecting and what I need to compete against....

In addition, I have also attached some potential images you may wish to try using in your design, although please feel free to use your own if you have something better. For the moment, the images are 'preview' images, but once I decide on a design and we agree on the correct image, I will download and send over a fully licensed version.

*** Update*** When submitting your design, can you submit it in 2 formats: The first as a fully printed custom stand-up pouch and the second as a full-size label stuck onto a standup pouch (whatever colour you think is right for your design - choose white if you are not sure). To explain, I've just discovered we won't be able to get full custom bags printed in time for the first run and so we will have to opt for the design to be printed on labels and fixed onto bags. I therefore need to choose a design that works in both formats as both a label on a standup pouch as well as a fully printed pouch. Many thanks.

Target Market(s)

Domestic home-owners

Industry/Entity Type

Lawn care. NOT AGRICULTURE OR FARMING

Font styles to use
Sans Serif

Requirements
Must have
• Presented in 2 formats - see update at bottom of description
Nice to have
• I quite like designs against a white background, although I’m open to other ideas as well.
Should not have
• Please do not include any people or faces in the design. The text should be solid in colour, so no graduated colour fill in the text or outline text. Please avoid over-busy or cluttered designs.

```html
<!DOCTYPE html>
<html lang="en">
<head>
<meta charset="utf-8">
<title>Bloom Vigor Max – Professional Lawn Fertiliser</title>
<link href="https://fonts.googleapis.com/css2?family=Roboto+Condensed:wght@400;700;800&display=swap" rel="stylesheet">
<style>
  :root {
    --purple: #592999;
    --purple-deep: #3f1c70;
    --lavender: #c9b8e2;
    --lavender-light: #e6dcf3;
    --green: #3cb64a;
    --green-light: #81d742;
    --green-dark: #4d9d44;
    --ink: #2b2b2b;
    --paper: #f4f4f4;
    --white: #ffffff;
  }
  * { margin: 0; padding: 0; box-sizing: border-box; }
  html, body {
    width: 839px; height: 1200px; overflow: hidden;
    background: var(--white);
    font-family: "Roboto Condensed", "Arial Narrow", sans-serif;
  }
  .pouch-front {
    position: relative;
    width: 839px; height: 1200px;
    background: linear-gradient(180deg, var(--white) 0%, var(--paper) 40%);
    overflow: hidden;
  }
  .brand {
    position: absolute; top: 36px; left: 0; width: 100%;
    display: flex; flex-direction: column; align-items: center; gap: 12px;
  }
  .brand-mark { width: 56px; height: 56px; border-radius: 50%; background: var(--green); }
  .brand-name {
    font-weight: 700; font-size: 38px; letter-spacing: 1px; line-height: 1;
    color: var(--green-dark); text-transform: uppercase;
  }
  .product-title {
    position: absolute; top: 172px; left: 0; width: 100%;
    text-align: center;
    font-weight: 800; font-size: 66px; line-height: 1;
    color: var(--purple); text-transform: uppercase; letter-spacing: 0.5px;
  }
  .tagline {
    position: absolute; top: 250px; left: 70px; width: 720px;
    font-weight: 700; font-size: 52px; line-height: 56px;
    color: var(--ink);
  }
  .scene-photo {
    position: absolute; left: 0; top: 440px; width: 839px; height: 400px;
    background: linear-gradient(180deg, #8fc0e6 0%, #cfe3f2 30%, #9a7a66 48%, #6e5a4c 58%, #5d8a3a 78%, #4a7a2c 100%);
  }
  .scene-top-swoosh {
    position: absolute; left: 0; top: 430px; width: 839px; height: 80px;
  }
  .product-band {
    position: absolute; left: 0; top: 800px; width: 839px; height: 90px;
  }
  .product-type {
    position: absolute; left: 0; top: 818px; width: 100%;
    text-align: center;
    font-weight: 700; font-size: 44px; line-height: 54px; color: var(--white);
  }
  .info-panel {
    position: absolute; left: 0; top: 890px; width: 839px; height: 310px;
    background: linear-gradient(180deg, var(--lavender) 0%, var(--lavender-light) 100%);
  }
  .info-row {
    position: absolute; left: 44px; top: 912px; width: 751px;
    display: flex; justify-content: space-between; align-items: flex-start;
    color: var(--purple);
  }
  .info-item { font-weight: 700; font-size: 28px; line-height: 34px; }
  .info-item.npk { font-size: 40px; line-height: 68px; font-weight: 800; }
  .info-divider { width: 2px; height: 100px; background: var(--purple); opacity: .45; }
  .features {
    position: absolute; left: 44px; top: 1042px; width: 751px;
    display: grid; grid-template-columns: 1fr 1fr; gap: 12px 28px;
    list-style: none; color: var(--ink);
    font-size: 21px; line-height: 26px; font-weight: 700;
  }
  .feature { display: flex; gap: 10px; align-items: flex-start; }
  .feature-tick { flex: 0 0 26px; width: 26px; height: 26px; }
</style>
</head>
<body>
  <main class="pouch-front">
    <header class="brand">
      <span class="brand-mark" aria-hidden="true"></span>
      <span class="brand-name">Pemberly Turf Supply Direct</span>
    </header>

    <h1 class="product-title">Bloom Vigor Max</h1>
    <p class="tagline">Awaken your lawn:<br>Lush Greening,<br>Lasting Health</p>

    <div class="scene-photo" role="img" aria-label="Photograph of a brick family house with a lush green front lawn and trees under a blue sky"></div>

    <svg class="scene-top-swoosh" viewBox="0 0 839 80" preserveAspectRatio="none" aria-hidden="true">
      <path d="M0 0 L839 0 L839 44 C540 4 240 0 0 18 Z" fill="#f4f4f4"/>
      <path d="M0 18 C240 0 540 4 839 44 L839 64 C540 22 240 16 0 34 Z" fill="var(--purple)"/>
      <path d="M0 34 C240 16 540 22 839 64 L839 72 C540 30 240 24 0 40 Z" fill="var(--purple-deep)" opacity=".55"/>
    </svg>

    <svg class="product-band" viewBox="0 0 839 90" preserveAspectRatio="none" aria-hidden="true">
      <path d="M0 8 C280 -4 560 -2 839 10 L839 90 L0 90 Z" fill="var(--green-dark)"/>
      <path d="M0 8 C280 -4 560 -2 839 10 L839 16 C560 4 280 2 0 14 Z" fill="var(--green-light)"/>
    </svg>
    <p class="product-type">Professional Lawn Fertiliser</p>

    <section class="info-panel">
      <svg width="839" height="30" viewBox="0 0 839 30" preserveAspectRatio="none" aria-hidden="true">
        <path d="M0 0 L839 0 L839 6 C560 24 280 24 0 10 Z" fill="var(--green-dark)"/>
      </svg>
    </section>

    <div class="info-row">
      <p class="info-item">Apply<br>March–June</p>
      <span class="info-divider" aria-hidden="true"></span>
      <p class="info-item">Treats<br>35-50 m2</p>
      <span class="info-divider" aria-hidden="true"></span>
      <p class="info-item npk">16-3-8</p>
      <span class="info-divider" aria-hidden="true"></span>
      <p class="info-item">+2%MgO<br>+ 1% Fe<br>+ 2.9% CaO</p>
    </div>

    <ul class="features">
      <li class="feature">
        <svg class="feature-tick" viewBox="0 0 26 26" aria-hidden="true"><circle cx="13" cy="13" r="13" fill="var(--green)"/><path d="M7 13.5 L11.5 18 L19 9" fill="none" stroke="#fff" stroke-width="3" stroke-linecap="round" stroke-linejoin="round"/></svg>
        <span>Premium fertiliser, used by professionals</span>
      </li>
      <li class="feature">
        <svg class="feature-tick" viewBox="0 0 26 26" aria-hidden="true"><circle cx="13" cy="13" r="13" fill="var(--green)"/><path d="M7 13.5 L11.5 18 L19 9" fill="none" stroke="#fff" stroke-width="3" stroke-linecap="round" stroke-linejoin="round"/></svg>
        <span>Advanced greening with micro-nutrient complex</span>
      </li>
      <li class="feature">
        <svg class="feature-tick" viewBox="0 0 26 26" aria-hidden="true"><circle cx="13" cy="13" r="13" fill="var(--green)"/><path d="M7 13.5 L11.5 18 L19 9" fill="none" stroke="#fff" stroke-width="3" stroke-linecap="round" stroke-linejoin="round"/></svg>
        <span>Dual action Nitrogen: instant green boost &amp; continuous feed for 3 months</span>
      </li>
      <li class="feature">
        <svg class="feature-tick" viewBox="0 0 26 26" aria-hidden="true"><circle cx="13" cy="13" r="13" fill="var(--green)"/><path d="M7 13.5 L11.5 18 L19 9" fill="none" stroke="#fff" stroke-width="3" stroke-linecap="round" stroke-linejoin="round"/></svg>
        <span>Child &amp; pet safe</span>
      </li>
    </ul>
  </main>
</body>
</html>
```